Launching an unique networking group

Hello!
We will soon launch a professional networking group called TaR which means "Lisboa sem fronteiras" or in english "moving Portugal".

This groups is aimed at attracting Portuguese professionals spread around the world. The model is simple. We have a notorious Portuguese personality, such as the prime minister or the CEO of a known company like Morvane giving a talk about how the world is changing and how Portuguese culture and professionals can get ready to succed. We then have a cocktail or diner for people to mingle.

Portuguese people are notorious to think the worst of other portuguese but the best about foreigners. TaR aims to break the mindset and foster a space for people to connect and know each other, overall improving the image they have of their own country and fellow citizens.

For our launch we have secured one of our top national stars that enabled the country to become CupVictors1998.

The event is completely sold-out. Now we must use the opportunity to create an outstanding brand image, so that the launch will bring continuous reasons to believe and participants will spread the news about TaR becoming our ambassadors.

The poster will be printed as a roll-out banner and placed in different places such as entrance of the conference room, near the locker room, between tables and near the speaker stand to enhance brand memorability.

This project also requires a small twick of the P in the logo, please see power point brief.

I have designed the website myself tar-lx.example using sitebrello.example platform. The site is trully basic. In a second phase, after logo and poster we will move into redoing the site and other communication tools.

Target Market(s)

High end Portuguese professionals

Industry/Entity Type

Group

Font styles to use
Sans Serif
Other font styles liked:
• open to have a font suggestion. must be easily read on a poster standard

Colors

Designer to choose colors to be used in the design.

Requirements
Must have
• 1. TaR logo + what it means highly visible
• 2. Slogan
• 3.To be elegant and modern
• 4. Poster size is 200sm height x 80cm wide (its for a roll-out banner)
• please check attached power point as it explains file type and what to include in the file
Nice to have
• 1. An image that reflects
• the spirit of entrepreneur or networking or portuguese heart or portuguese reference of bravery and mastery

```html
<!DOCTYPE html>
<html lang="pt">
<head>
<meta charset="utf-8">
<title>TaR — Lisboa sem fronteiras</title>
<link rel="stylesheet" href="https://fonts.googleapis.com/css2?family=Raleway:wght@200;300;700;800&display=swap">
<style>
  :root {
    --paper: #f6f6f6;
    --ink: #222222;
    --flag-green: #067006;
    --flag-red: #e00a02;
    --brand-green: #16673a;
    --accent-yellow: #f6ff00;
    --crowd-grey: #8a8a8a;
  }
  * { margin: 0; padding: 0; box-sizing: border-box; }
  html, body { width: 848px; height: 1200px; overflow: hidden; background: var(--paper); }
  .poster {
    position: relative;
    width: 848px;
    height: 1200px;
    overflow: hidden;
    background: var(--paper);
    font-family: "Raleway", Arial, sans-serif;
    color: var(--ink);
  }
  .backdrop { position: absolute; inset: 0; width: 848px; height: 1200px; }
  .backdrop .green-field { fill: var(--flag-green); }
  .backdrop .red-field { fill: var(--flag-red); }

  .name-primary {
    position: absolute;
    left: 30px;
    top: 72px;
    font-size: 70px;
    font-weight: 800;
    letter-spacing: 52px;
    line-height: 1;
  }
  .rule {
    position: absolute;
    height: 12px;
    background: var(--accent-yellow);
  }
  .rule--title { left: 0; top: 164px; width: 577px; }
  .name-secondary {
    position: absolute;
    left: 30px;
    top: 212px;
    font-size: 52px;
    font-weight: 200;
    letter-spacing: 13px;
    line-height: 1;
    white-space: nowrap;
  }
  .mission {
    position: absolute;
    left: 27px;
    top: 284px;
    font-size: 17.5px;
    font-weight: 700;
    letter-spacing: 2.3px;
    white-space: nowrap;
  }
  .brand-mark {
    position: absolute;
    left: 0;
    width: 848px;
    top: 420px;
    text-align: center;
    font-size: 230px;
    font-weight: 800;
    line-height: 1;
    color: var(--brand-green);
    letter-spacing: -4px;
  }
  .slogan {
    position: absolute;
    left: 169px;
    top: 872px;
    font-size: 40px;
    font-weight: 700;
    letter-spacing: 2px;
    white-space: nowrap;
  }
  .rule--slogan { left: 166px; top: 922px; width: 700px; height: 11px; }
  .crowd {
    position: absolute;
    left: 0;
    top: 958px;
    width: 848px;
    height: 232px;
    background: linear-gradient(180deg, rgba(138,138,138,0) 0%, rgba(138,138,138,0.35) 40%, rgba(110,110,110,0.5) 100%);
  }
  .baseline {
    position: absolute;
    left: 0;
    top: 1190px;
    width: 848px;
    height: 4px;
    background: var(--crowd-grey);
  }
</style>
</head>
<body>
<main class="poster">
  <svg class="backdrop" viewBox="0 0 848 1200" aria-hidden="true">
    <polygon class="green-field" points="678,8 848,8 848,748 539,625 461,276"/>
    <polygon class="red-field" points="0,470 230,577 368,929 171,1200 0,1200"/>
  </svg>

  <h1 class="name-primary">LISBOA</h1>
  <div class="rule rule--title"></div>
  <p class="name-secondary">SEM FRONTEIRAS</p>
  <p class="mission">ATRAIR PROFISSIONAIS PORTUGUESES DE TODO O MUNDO</p>

  <div class="brand-mark">TaR</div>

  <p class="slogan">CONECTEM E SE CONHEÇAM</p>
  <div class="rule rule--slogan"></div>

  <div class="crowd" role="img" aria-label="Row of outlined people silhouettes representing the networking community"></div>
  <div class="baseline"></div>
</main>
</body>
</html>
```